I need a new business card design for my pharmacy.

I need a business card design. I will include my logo.
The card needs to be readable. I prefer to have my logo on one side along with my website, the other side includes the other information. Please use combination of black, neon green, white, and silver. This needs to catch the eye but yet be clearly visible and legible. Thanks

Industry/Entity Type

Pharmacy

Contact Information for Business Card

It needs to have the following information listed:
Mel's Apothecary Owner/Pharm D.
7134 North Brook Lane
Sioux Falls, SD 57231
Phone 605-318-6207
Fax 605-318-6209
email: mel@melsapothecary-example.com
www.melsapothecary-example.com
Store hours Monday-Friday 8 am- 7 pm
Saturday 8 am- 12 pm
Sunday Closed
Please utilize the colors black, white, and neon green, maybe silver.

Requirements
Must have
• It needs to be easily readable!
Nice to have
• It should catch the eye.
Should not have
• Do not use any other colors except listed: black, neon green, white, & silver.

```html
<!DOCTYPE html>
<html lang="en">
<head>
<meta charset="utf-8">
<title>Mel's Apothecary – Business Card</title>
<link href="https://fonts.googleapis.com/css2?family=Source+Sans+3:wght@400;600;700&display=swap" rel="stylesheet">
<style>
  :root {
    --bg: #9a9a98;
    --black: #0b0b0b;
    --charcoal: #2f2f30;
    --dark: #222223;
    --green: #a3cc39;
    --white: #ffffff;
    --silver: #d4d4d4;
    --grey-text: #e6e6e6;
    --embossed: #3a3a3b;
  }
  * { margin: 0; padding: 0; box-sizing: border-box; }
  html, body { width: 1200px; height: 900px; overflow: hidden; }
  body {
    background: var(--bg);
    font-family: "Source Sans 3", "Myriad Pro", Arial, sans-serif;
    position: relative;
  }
  .card {
    position: absolute;
    left: 270px;
    width: 660px;
    height: 377px;
    overflow: hidden;
    box-shadow: 0 4px 14px rgba(0,0,0,0.25);
  }

  /* Back side: name + store hours */
  .card-back { top: 52px; background: var(--dark); }
  .brand-bar {
    height: 205px;
    display: flex;
    align-items: center;
    justify-content: center;
    gap: 18px;
  }
  .brand-mark {
    width: 34px; height: 34px; border-radius: 50%;
    background: var(--green);
  }
  .brand-name {
    font-size: 44px;
    font-weight: 600;
    color: var(--embossed);
    letter-spacing: 0.5px;
  }
  .hours-band {
    height: 172px;
    background: var(--green);
    color: var(--white);
    text-align: center;
    padding-top: 28px;
  }
  .hours-title { font-size: 25px; font-weight: 700; letter-spacing: 0.5px; margin-bottom: 6px; }
  .hours-line { font-size: 21px; line-height: 1.22; }
  .hours-closed { font-weight: 700; }

  /* Front side: contact */
  .card-front { top: 471px; background: var(--charcoal); }
  .shapes { position: absolute; inset: 0; }
  .front-name {
    position: absolute;
    left: 30px; top: 166px;
    width: 240px;
    font-size: 30px;
    font-weight: 700;
    color: var(--white);
    line-height: 1.1;
  }
  .contact {
    position: absolute;
    right: 32px; top: 40px;
    text-align: right;
    color: var(--grey-text);
  }
  .contact-name { font-size: 26px; font-weight: 700; color: var(--green); line-height: 1.05; }
  .contact-title { font-size: 18px; margin-bottom: 16px; }
  .contact-address { font-size: 18px; line-height: 1.35; margin-bottom: 14px; }
  .contact-row {
    display: flex; justify-content: flex-end; align-items: center; gap: 10px;
    font-size: 17px; line-height: 1.4;
  }
  .contact-row svg { width: 14px; height: 14px; fill: var(--green); flex: none; }
</style>
</head>
<body>

<section class="card card-back" aria-label="Business card back">
  <div class="brand-bar">
    <span class="brand-mark"></span>
    <span class="brand-name">Mel's Apothecary</span>
  </div>
  <div class="hours-band">
    <p class="hours-title">STORE HOURS</p>
    <p class="hours-line">Monday-Friday 8 am- 7 pm</p>
    <p class="hours-line">Saturday 8 am- 12 pm</p>
    <p class="hours-line hours-closed">Sunday Closed</p>
  </div>
</section>

<section class="card card-front" aria-label="Business card front">
  <svg class="shapes" viewBox="0 0 660 377" preserveAspectRatio="none" aria-hidden="true">
    <path d="M0 0 H262 C345 90 335 280 245 377 H0 Z" fill="var(--silver)"/>
    <path d="M250 0 H278 C352 90 345 210 298 290 C325 200 320 80 250 0 Z" fill="var(--green)"/>
    <path d="M0 0 H250 C330 80 330 260 220 377 H0 Z" fill="var(--black)"/>
  </svg>
  <p class="front-name">Mel's Apothecary</p>
  <div class="contact">
    <p class="contact-name">Mel's Apothecary</p>
    <p class="contact-title">Owner/Pharm D.</p>
    <p class="contact-address">7134 North Brook Lane<br>Sioux Falls, SD 57231</p>
    <p class="contact-row">605-318-6207
      <svg viewBox="0 0 16 16"><path d="M3 1l3 3-1.5 2a9 9 0 0 0 5.5 5.5L12 10l3 3-2 2C7 15 1 9 1 3z"/></svg></p>
    <p class="contact-row">605-318-6209
      <svg viewBox="0 0 16 16"><path d="M4 1h6l2 2v3h2v9H2V6h2zM5 2v4h6V3.5L9.5 2zM4 9h2v2H4zm3 0h2v2H7zm3 0h2v2h-2z"/></svg></p>
    <p class="contact-row">mel@melsapothecary-example.com
      <svg viewBox="0 0 16 16"><path d="M1 3h14v10H1zm1.5 1.3v.4L8 9l5.5-4.3v-.4z"/></svg></p>
    <p class="contact-row">www.melsapothecary-example.com
      <svg viewBox="0 0 16 16"><path d="M6 10l4-4 1 1-4 4zM3 9l2-2 1 1-2 2a1.4 1.4 0 0 0 2 2l2-2 1 1-2 2a2.8 2.8 0 0 1-4-4zm10-2l-2 2-1-1 2-2a1.4 1.4 0 0 0-2-2L8 6 7 5l2-2a2.8 2.8 0 0 1 4 4z"/></svg></p>
  </div>
</section>

</body>
</html>
```